Tallowbrook Aesthetic Medic is the title and the name of the business

Chatterleaf advertising: keep
To those dimensions

Aimed at Caucasian women between the ages of 18 - 60 interested in beauty and cosmetic injectables. Will be boosted on chatterleaf which is my advertising platform.

Name: Tallowbrook Aesthetic Medic
0491 570 318

Forehead $58
Frown lines $116
Crows feet $116
Lip fillers $380

I would like to have a beautiful girl that suits the picture.

Target Market(s)

Females between 18 - 60 interested in Lumiset and cosmetic fillers
Prefer Caucasian as that's the majority of population

Industry/Entity Type

Beauty Salon

Font styles to use
Serif
Script

Colors
e667a6
eea4c8
f9d9e8
fee18a
fbf289
fbee3d
cadf82
cedeed
85cae6

Requirements
Must have
• Name: Tallowbrook Aesthetic Medic
• Phone number: 0491 570 381
• Prices:
• Forehead $58
• Frown lines $116
• Crows feet $116
• Lip fillers $380
• Picture of female that is very beautiful
Nice to have
• Not a cartoon or anything else that's not a real picture of a female
Should not have
• No cartoon pictures. Proper picture of women

```html
<!DOCTYPE html>
<html lang="en">
<head>
<meta charset="utf-8">
<title>Tallowbrook Aesthetic Medic – Chatterleaf Banner</title>
<link rel="stylesheet" href="https://fonts.googleapis.com/css2?family=Parisienne&display=swap">
<style>
  :root {
    --hot-pink: #e667a6;
    --soft-pink: #eea4c8;
    --blush: #f9d9e8;
    --butter: #fee18a;
    --lemon: #fbf289;
    --sun: #fbee3d;
    --lime: #cadf82;
    --mist: #cedeed;
    --sky: #85cae6;
    --ink: #1c1418;
    --page: #ffffff;
  }
  * { margin: 0; padding: 0; box-sizing: border-box; }
  html, body {
    width: 1200px; height: 903px; overflow: hidden;
    background: var(--page);
  }
  .canvas { position: relative; width: 1200px; height: 903px; }
  .banner {
    position: absolute; left: 157px; top: 288px;
    width: 886px; height: 328px; overflow: hidden;
    background: var(--lime);
    box-shadow: 2px 3px 5px rgba(0,0,0,.35);
    font-family: "Parisienne", cursive;
    color: var(--ink);
  }
  .brand-panel {
    position: absolute; left: 0; top: 0; width: 240px; height: 316px;
  }
  .brand-panel__shape { position: absolute; left: 0; top: 0; }
  .brand-name {
    position: absolute; left: 0; top: 14px; width: 233px;
    text-align: center; font-size: 22px; font-weight: 400; line-height: 38px;
  }
  .brand-phone {
    position: absolute; left: 22px; top: 90px;
    display: flex; align-items: center; gap: 4px;
    font-size: 25px; line-height: 30px; letter-spacing: .5px;
    white-space: nowrap;
  }
  .brand-phone__icon { flex: 0 0 auto; width: 17px; height: 19px; }
  .price-ribbon {
    position: absolute; left: 224px; width: 257px; height: 48px;
  }
  .price-ribbon__shape { position: absolute; left: 0; top: 0; width: 100%; height: 100%; }
  .price-ribbon__label {
    position: absolute; left: 22px; top: 4px;
    font-size: 27px; line-height: 40px; white-space: nowrap;
  }
  .price-ribbon--bold .price { color: var(--butter); }
  .ribbon-forehead { top: 33px; }
  .ribbon-frown { top: 105px; }
  .ribbon-crows { top: 172px; }
  .ribbon-lips { top: 243px; left: 206px; }
  .model-photo {
    position: absolute; left: 478px; top: 0; width: 408px; height: 316px;
    background:
      radial-gradient(ellipse 26% 40% at 45% 48%, #ead0c0 0%, #d9b3a0 60%, rgba(217,179,160,0) 100%),
      radial-gradient(ellipse 60% 80% at 50% 45%, #8a5a3e 0%, #6e432c 55%, #4a2c1d 100%);
  }
  .color-stripe {
    position: absolute; left: 0; bottom: 0; width: 886px; height: 12px;
    background: linear-gradient(90deg, var(--hot-pink) 0%, var(--blush) 20%, var(--butter) 38%, var(--sky) 55%, var(--sun) 72%, var(--soft-pink) 100%);
  }
</style>
</head>
<body>
<div class="canvas">
  <section class="banner">
    <div class="brand-panel">
      <svg class="brand-panel__shape" width="240" height="316" viewBox="0 0 240 316" aria-hidden="true">
        <path d="M0 0 H228 Q232 6 228 12 Q232 18 228 24 Q232 30 228 36 Q232 42 227 48 Q231 54 226 60 Q230 66 225 72 Q229 78 224 84 Q228 90 223 96 Q227 102 222 108 Q226 114 221 120 Q225 126 220 132 Q224 138 219 144 Q223 150 218 156 Q222 162 217 168 Q221 174 216 180 Q220 186 215 192 Q219 198 214 204 Q218 210 213 216 Q217 222 212 228 Q216 234 211 240 Q215 246 210 252 Q214 258 209 264 Q213 270 208 276 Q212 282 207 288 Q211 294 206 300 Q210 306 205 316 H0 Z" fill="var(--lemon)"/>
      </svg>
      <h1 class="brand-name">Tallowbrook Aesthetic<br>Medic</h1>
      <p class="brand-phone">
        <svg class="brand-phone__icon" viewBox="0 0 18 20" aria-hidden="true"><path d="M4 1 L7 5 L5 8 Q7 12 10 14 L13 12 L17 15 L15 19 Q7 18 2 8 Q1 4 4 1 Z" fill="var(--hot-pink)"/></svg>
        <span>0491570381</span>
      </p>
    </div>

    <div class="price-ribbon price-ribbon--light ribbon-forehead">
      <svg class="price-ribbon__shape" viewBox="0 0 257 48" preserveAspectRatio="none" aria-hidden="true"><path d="M0 2 H238 L250 48 H0 L12 25 Z" fill="var(--blush)"/></svg>
      <span class="price-ribbon__label">Forehead <span class="price">$58</span></span>
    </div>
    <div class="price-ribbon price-ribbon--bold ribbon-frown">
      <svg class="price-ribbon__shape" viewBox="0 0 257 48" preserveAspectRatio="none" aria-hidden="true"><path d="M0 0 H240 L256 24 L240 48 H0 Z" fill="var(--hot-pink)"/></svg>
      <span class="price-ribbon__label">Frown lines <span class="price">$116</span></span>
    </div>
    <div class="price-ribbon price-ribbon--light ribbon-crows">
      <svg class="price-ribbon__shape" viewBox="0 0 257 48" preserveAspectRatio="none" aria-hidden="true"><path d="M6 0 H242 L256 48 H6 L16 24 Z" fill="var(--blush)"/></svg>
      <span class="price-ribbon__label">Crows feet <span class="price">$116</span></span>
    </div>
    <div class="price-ribbon price-ribbon--bold ribbon-lips">
      <svg class="price-ribbon__shape" viewBox="0 0 257 48" preserveAspectRatio="none" aria-hidden="true"><path d="M0 8 L230 0 L256 42 L6 48 Z" fill="var(--hot-pink)"/></svg>
      <span class="price-ribbon__label">Lip fillers <span class="price">$380</span></span>
    </div>

    <div class="model-photo" role="img" aria-label="Photograph of a woman with long curly brown hair, pink lips and purple nails, wearing a jewelled drop earring"></div>
    <div class="color-stripe"></div>
  </section>
</div>
</body>
</html>
```